We need to redo the www.larkvento.com website. Content will be greatly reduced. LarkVento is a marketing consulting and marketing automation company that provides services to limousine and executive car service companies. Our main competitor's site is http://www.quillharborpartners.com/, which I like very much. I would like larkvento.com to have a similar format and a more simple user interface. We would need a home page, product page, services page, resource page, blog, about the company, and contact us page. Our colors are currently the green/blue of the logo, but we are happy to change colors and/or logo if a compelling design warranted - as a matter of fact, we are quite tired of the blue and green. :) I will fit content to design, but there are, you will see, a number of products and services that need to be covered. Again, I like the way the competitor arranged things so everything was easy to find. We want a wide width or "one page" format that uses a lot of images - we will purchase images as required.
Updates

We'd like the site to look more similar to the style of quillharborpartners.com please :) Thank you!

Industry/Entity Type

Marketing

```html
<!DOCTYPE html>
<html lang="en">
<head>
<meta charset="utf-8">
<title>LarkVento — Marketing for Executive Car Services</title>
<link rel="stylesheet" href="https://fonts.googleapis.com/css2?family=Open+Sans:ital,wght@0,400;0,600;0,700;1,400&display=swap">
<style>
:root{
  --green:#5b9a1a;
  --green-light:#7db61f;
  --green-dark:#467a10;
  --ink:#3d3d3d;
  --text:#666;
  --muted:#888;
  --page:#ececec;
  --card:#fff;
  --dark:#262626;
  --footer:#1b1b1b;
  --line:#cfcfcf;
}
*{box-sizing:border-box;margin:0;padding:0}
html,body{width:1200px;height:2980px;overflow:hidden}
body{font-family:"Open Sans",Arial,sans-serif;color:var(--text);background:var(--page);position:relative}
.abs{position:absolute}

/* header */
.site-header{position:absolute;left:0;top:0;width:1200px;height:98px;background:#fff}
.brand{position:absolute;left:180px;top:36px;display:flex;align-items:center;gap:10px;font-weight:700;font-size:24px;color:var(--green);letter-spacing:.5px}
.brand-dot{width:22px;height:22px;border-radius:50%;background:var(--green)}
.contact-tab{position:absolute;left:632px;top:0;width:330px;height:40px;background:var(--green);border-radius:0 0 4px 4px;color:#fff;font-size:14px;display:flex;align-items:center;justify-content:center;gap:6px}
.contact-tab small{font-size:11px;opacity:.85}
.main-nav{position:absolute;right:178px;top:64px;display:flex;gap:18px;font-size:12.5px;color:var(--ink)}

/* hero */
.hero{position:absolute;left:0;top:98px;width:1200px;height:418px}
.hero-photo{position:absolute;inset:0;background:linear-gradient(180deg,#5f7376 0%,#3c4a4c 45%,#1d2324 100%)}
.hero-arrow{position:absolute;top:170px;width:54px;height:64px;background:rgba(0,0,0,.35);display:flex;align-items:center;justify-content:center}
.hero-arrow.left{left:0}.hero-arrow.right{right:0}
.hero-copy{position:absolute;left:0;top:250px;width:1200px;text-align:center;color:#fff;text-shadow:0 1px 3px rgba(0,0,0,.5)}
.hero-copy p{font-size:25px}
.hero-copy strong{display:block;font-size:24px;font-weight:700;margin-top:4px}
.btn{display:inline-block;background:var(--green);color:#fff;font-size:15px;border-radius:2px}
.hero-btn{position:absolute;left:520px;top:340px;width:142px;height:38px;line-height:38px;text-align:center;background:linear-gradient(#6ea82a,#4d8a14)}

/* process */
.process{position:absolute;left:0;top:516px;width:1200px;height:366px;background:var(--page)}
.section-title{font-size:28px;font-weight:400;color:#666;text-align:center}
.section-title b{font-weight:700;color:#555}
.process .section-title{position:absolute;top:38px;width:100%}
.tagline{position:absolute;top:84px;width:100%;text-align:center;font-size:12px;font-style:italic;color:var(--muted)}
.process-icon{position:absolute;top:140px}
.connector{position:absolute;height:2px;background:#bdbdbd}
.step{position:absolute;top:228px;width:262px}
.step h3{font-size:18px;font-weight:400;color:#444;margin-bottom:8px}
.step p{font-size:11px;line-height:18px;color:var(--muted)}

/* game-changer band */
.band{position:absolute;left:0;top:882px;width:1200px;height:414px;background:var(--dark);overflow:hidden}
.screen-frame{position:absolute;left:112px;top:52px;width:974px;height:420px;background:#111;border-radius:18px}
.screen-cam{position:absolute;left:484px;top:10px;width:6px;height:6px;border-radius:50%;background:#333}
.screen{position:absolute;left:40px;top:38px;width:894px;height:340px;background:linear-gradient(180deg,#6ea812 0%,#5b9a0e 100%)}
.band-icon{position:absolute;top:70px}
.band-line{position:absolute;top:112px;height:3px;background:#fff}
.band h2{position:absolute;top:176px;width:100%;text-align:center;color:#fff;font-size:29px;font-weight:400}
.band h2 b{font-weight:700}
.band p{position:absolute;top:232px;left:90px;width:714px;text-align:center;color:#e6f2d4;font-size:12.5px;line-height:20px}

/* team */
.team{position:absolute;left:0;top:1296px;width:1200px;height:430px}
.team .section-title{position:absolute;top:52px;width:100%}
.title-rule{position:absolute;top:70px;height:1px;background:var(--line)}
.team .sub{position:absolute;top:98px;width:100%;text-align:center;font-size:13px;color:#555}
.member{position:absolute;top:138px;width:176px}
.member-photo{width:176px;height:164px;background:#fff;padding:6px;box-shadow:0 1px 4px rgba(0,0,0,.18);position:relative}
.member-photo div{width:100%;height:100%;background:linear-gradient(160deg,#9a9a9a,#3a3a3a)}
.member-badge{position:absolute;right:6px;bottom:6px;width:34px;height:30px;background:var(--green)}
.member h4{font-size:14px;font-weight:600;color:#555;margin-top:14px}
.member span{font-size:11.5px;color:var(--muted)}
.dots{position:absolute;top:380px;left:574px;display:flex;gap:6px}
.dots i{width:7px;height:7px;border-radius:50%;background:#aaa}
.dots i.on{background:var(--green)}

/* cards */
.card{position:absolute;background:var(--card);box-shadow:0 1px 2px rgba(0,0,0,.08)}
.plus{position:absolute;left:0;top:0;width:24px;height:24px;background:var(--green);color:#fff;font-size:20px;line-height:22px;text-align:center;font-weight:700}
.card h2{font-size:24px;font-weight:400;color:#444;margin-bottom:12px}
.card h2 b{font-weight:700}
.card .lead{font-size:11.5px;line-height:19px;color:var(--green);margin-bottom:6px}
.card .body{font-size:11.5px;line-height:19px;color:var(--muted)}
.card-inner{position:absolute;left:40px;top:42px;width:270px}

/* contact */
.contact .intro{font-size:11px;color:var(--green);margin-top:-4px}
.field{position:absolute;background:#f2f2f2;border:1px solid #dcdcdc;font-size:11px;color:#666;padding:10px}
.submit{position:absolute;left:40px;top:222px;width:92px;height:40px;line-height:40px;text-align:center;font-size:14px;font-weight:600;background:linear-gradient(#6ea82a,#4d8a14)}

/* news & blog */
.news-item{display:flex;gap:14px;margin-bottom:20px}
.date{width:62px;height:62px;background:linear-gradient(#6aa31f,#3f7a0c);color:#fff;text-align:center;border:3px solid #d8e8c4;flex:none}
.date b{display:block;font-size:22px;line-height:30px;margin-top:2px}
.date span{font-size:10px;letter-spacing:1px}
.news-item h5{font-size:11.5px;font-weight:400;color:var(--green);margin-bottom:4px}
.news-item p,.post p{font-size:11.5px;line-height:18px;color:#555}
.news-item a{font-size:11.5px;color:#333;font-weight:600;text-decoration:none}
.post{margin-bottom:20px}
.post .by{color:var(--green);font-size:11.5px;margin-top:6px}

/* footer */
.site-footer{position:absolute;left:0;top:2770px;width:1200px;height:210px;background:var(--footer);border-top:4px solid var(--green)}
.footer-brand{position:absolute;left:236px;top:38px;display:flex;align-items:center;gap:10px;font-weight:700;font-size:24px;color:var(--green)}
.copyright{position:absolute;left:268px;top:88px;font-size:10.5px;color:#aaa}
.footer-nav{position:absolute;right:236px;top:38px;font-size:10.5px;color:#bbb}
.social{position:absolute;right:236px;top:88px;display:flex;gap:30px;font-size:10.5px;color:var(--green-light)}
</style>
</head>
<body>

<header class="site-header">
  <div class="brand"><span class="brand-dot"></span>LarkVento</div>
  <div class="contact-tab"><small>Toll-Free :</small> 555-014-2290 / info@larkvento.com</div>
  <nav class="main-nav">
    <span>Integrated Marketing</span><span>Services</span><span>News &amp; Events</span><span>RideKeepers™</span><span>Blog</span><span>Contact Us</span>
  </nav>
</header>

<section class="hero">
  <div class="hero-photo" role="img" aria-label="Team of business professionals in suits standing in front of a city skyline, toned in blue-grey"></div>
  <div class="hero-arrow left"><svg width="16" height="28" viewBox="0 0 16 28"><path d="M14 2 2 14l12 12" fill="none" stroke="#fff" stroke-width="2"/></svg></div>
  <div class="hero-arrow right"><svg width="16" height="28" viewBox="0 0 16 28"><path d="M2 2l12 12L2 26" fill="none" stroke="#fff" stroke-width="2"/></svg></div>
  <div class="hero-copy">
    <p>We Have A Passion For What We Do. Let Us Do What We Do Best ...</p>
    <strong>Lark VENTO.</strong>
  </div>
  <a class="btn hero-btn">Learn more &gt;</a>
</section>

<section class="process">
  <h2 class="section-title">Our unique <b>Marketing Process</b></h2>
  <div class="tagline">And we mean that.</div>

  <svg class="process-icon" style="left:330px" width="56" height="44" viewBox="0 0 56 44"><rect x="19" y="2" width="18" height="10" rx="2" fill="none" stroke="#5b9a1a" stroke-width="4"/><rect x="2" y="10" width="52" height="32" rx="3" fill="#5b9a1a"/><rect x="2" y="22" width="52" height="3" fill="#fff"/><rect x="24" y="19" width="8" height="9" fill="#5b9a1a" stroke="#fff" stroke-width="2"/></svg>
  <div class="connector" style="left:424px;top:162px;width:108px"></div>
  <svg class="process-icon" style="left:582px" width="46" height="46" viewBox="0 0 46 46"><circle cx="23" cy="23" r="21" fill="#5b9a1a"/><ellipse cx="23" cy="23" rx="9" ry="21" fill="none" stroke="#fff" stroke-width="2"/><path d="M2 23h42M6 12h34M6 34h34" stroke="#fff" stroke-width="2"/></svg>
  <div class="connector" style="left:672px;top:162px;width:108px"></div>
  <svg class="process-icon" style="left:812px" width="64" height="50" viewBox="0 0 64 50"><path d="M2 4h10l8 30h34l6-22H16" fill="none" stroke="#5b9a1a" stroke-width="4"/><path d="M20 18h36M22 26h32M30 12v22M40 12v22" stroke="#5b9a1a" stroke-width="2"/><circle cx="24" cy="43" r="4" fill="#5b9a1a"/><circle cx="50" cy="43" r="4" fill="#5b9a1a"/></svg>

  <div class="step" style="left:234px"><h3>Researching</h3><p>Lorem ipsum dolor sit amet, consectetur adipisicing elit, sed do eiusmod tempor incididunt ut labore et dolore magna aliqua.</p></div>
  <div class="step" style="left:486px"><h3>Networking</h3><p>Lorem ipsum dolor sit amet, consectetur adipisicing elit, sed do eiusmod tempor incididunt ut labore et dolore magna aliqua.</p></div>
  <div class="step" style="left:734px"><h3>Delivering</h3><p>Lorem ipsum dolor sit amet, consectetur adipisicing elit, sed do eiusmod tempor incididunt ut labore et dolore magna aliqua.</p></div>
</section>

<section class="band">
  <div class="screen-frame">
    <span class="screen-cam"></span>
    <div class="screen">
      <svg class="band-icon" style="left:100px" width="78" height="60" viewBox="0 0 56 44"><rect x="19" y="2" width="18" height="10" rx="2" fill="none" stroke="#fff" stroke-width="4"/><rect x="2" y="10" width="52" height="32" rx="3" fill="#fff"/><rect x="2" y="22" width="52" height="3" fill="#6ea812"/><rect x="24" y="19" width="8" height="9" fill="#fff" stroke="#6ea812" stroke-width="2"/></svg>
      <div class="band-line" style="left:222px;width:118px"></div>
      <svg class="band-icon" style="left:414px;top:72px" width="68" height="68" viewBox="0 0 46 46"><circle cx="23" cy="23" r="21" fill="#fff"/><ellipse cx="23" cy="23" rx="9" ry="21" fill="none" stroke="#6ea812" stroke-width="2"/><path d="M2 23h42M6 12h34M6 34h34" stroke="#6ea812" stroke-width="2"/></svg>
      <div class="band-line" style="left:556px;width:118px"></div>
      <svg class="band-icon" style="left:700px;top:64px" width="92" height="72" viewBox="0 0 64 50"><path d="M2 4h10l8 30h34l6-22H16" fill="none" stroke="#fff" stroke-width="3.5"/><path d="M20 18h36M22 26h32M30 12v22M40 12v22" stroke="#fff" stroke-width="2"/><circle cx="24" cy="43" r="4" fill="#fff"/><circle cx="50" cy="43" r="4" fill="#fff"/></svg>
      <h2>We're Not Just Raising the Stakes. We're <b>Changing the Game</b>.</h2>
      <p>We are a Fan Factory. We create opportunities for people to get excited about your company, which drives the creation of transactional value for your business. We create Fans - not just social page fans - but people who pay attention to you and spend more money with you.</p>
    </div>
  </div>
</section>

<section class="team">
  <div class="title-rule" style="left:142px;width:150px"></div>
  <div class="title-rule" style="left:908px;width:150px"></div>
  <h2 class="section-title">A very <b>Diversed Proffesionals Team</b> we have</h2>
  <div class="sub">We'll some of us anyways</div>

  <div class="member" style="left:232px"><div class="member-photo"><div role="img" aria-label="Portrait photo of Owen Pratley"></div><span class="member-badge"></span></div><h4>Owen Pratley</h4><span>Project Analyst</span></div>
  <div class="member" style="left:418px"><div class="member-photo"><div role="img" aria-label="Portrait photo of Milo Varek"></div><span class="member-badge"></span></div><h4>Milo Varek</h4><span>Marketing Developer</span></div>
  <div class="member" style="left:602px"><div class="member-photo"><div role="img" aria-label="Portrait photo of Tessan Doyle"></div><span class="member-badge"></span></div><h4>Tessan Doyle</h4><span>Client Relationship Manager</span></div>
  <div class="member" style="left:786px"><div class="member-photo"><div role="img" aria-label="Portrait photo of Callum Reyes"></div><span class="member-badge"></span></div><h4>Callum Reyes</h4><span>Project Co-ordinator</span></div>

  <div class="dots"><i class="on"></i><i></i><i></i><i></i></div>
</section>

<article class="card" style="left:236px;top:1746px;width:358px;height:286px">
  <span class="plus">+</span>
  <div class="card-inner">
    <h2><b>About</b> our company</h2>
    <p class="lead">Lorem ipsum dolor sit amet, consectetur adipisicing elit, sed do eiusmod tempor incididunt ut labore et dolore magna aliqua.</p>
    <p class="body">Lorem ipsum dolor sit amet, consectetur adipisicing elit, sed do eiusmod tempor incididunt ut labore et dolore magna aliqua. Lorem ipsum dolor sit amet, consectetur adipisicing elit, sed do eiusmod tempor incididunt ut labore et dolore magna aliqua.</p>
  </div>
</article>
<article class="card" style="left:606px;top:1746px;width:358px;height:286px">
  <span class="plus">+</span>
  <div class="card-inner">
    <h2><b>Services</b> we provide</h2>
    <p class="lead">Lorem ipsum dolor sit amet, consectetur adipisicing elit, sed do eiusmod tempor incididunt ut labore et dolore magna aliqua.</p>
    <p class="body">Lorem ipsum dolor sit amet, consectetur adipisicing elit, sed do eiusmod tempor incididunt ut labore et dolore magna aliqua. Lorem ipsum dolor sit amet, consectetur adipisicing elit, sed do eiusmod tempor incididunt ut labore et dolore magna aliqua.</p>
  </div>
</article>

<section class="card contact" style="left:236px;top:2074px;width:728px;height:302px">
  <div class="card-inner" style="width:600px">
    <h2><b>Contact</b> us</h2>
    <p class="intro">Fill the below form to enquire about your project to start with us.</p>
  </div>
  <div class="field" style="left:40px;top:122px;width:296px;height:40px">Name</div>
  <div class="field" style="left:40px;top:170px;width:296px;height:40px">Email id</div>
  <div class="field" style="left:360px;top:122px;width:296px;height:88px">Query</div>
  <a class="btn submit">Submit</a>
</section>

<section class="card" style="left:236px;top:2424px;width:358px;height:284px">
  <span class="plus">+</span>
  <div class="card-inner">
    <h2><b>News</b> discuss</h2>
    <div class="news-item"><div class="date"><b>12</b><span>SEP</span></div><div><h5>News headline1</h5><p>Lorem ipsum dolor sit amet, sed do eiusmod tempor sit amet.</p><a>Read Details &gt;</a></div></div>
    <div class="news-item"><div class="date"><b>23</b><span>SEP</span></div><div><h5>News headline2</h5><p>Lorem ipsum dolor sit amet, sed do eiusmod tempor sit amet.</p><a>Read Details &gt;</a></div></div>
  </div>
</section>
<section class="card" style="left:606px;top:2424px;width:358px;height:284px">
  <span class="plus">+</span>
  <div class="card-inner">
    <h2><b>Blog</b> posted</h2>
    <div class="post"><p>Lorem ipsum dolor sit amet, consectetur adipisicing elit, sed do eiusmod tempor incididunt.</p><p class="by">By, Ned Halloway, 14 Sep, 2014</p></div>
    <div class="post"><p>Lorem ipsum dolor sit amet, consectetur adipisicing elit, sed do eiusmod tempor incididunt.</p><p class="by">By, Ned Halloway, 21 Sep, 2014</p></div>
  </div>
</section>

<footer class="site-footer">
  <div class="footer-brand"><span class="brand-dot"></span>LarkVento</div>
  <div class="copyright">Copyright©2014 &nbsp;|&nbsp; Terms &amp; Policy</div>
  <nav class="footer-nav">Integrated Marketing | Services | News &amp; Events | RideKeepers™ | Blog | Contact Us</nav>
  <div class="social"><span>Chatterline</span><span>Circlepage</span><span>RSS</span><span>Mail</span></div>
</footer>

</body>
</html>
```